Kestrel Summit 2019 Enemies of the End-Times Church Flyer

We want a church conference flyer designed. We are looking for a professional, yet catchy design that uses our brand colors and logo creatively while communicating key information of the event effectively. <br/>The flyer must include all of the following:<br/>Title: Kestrel Summit 2019<br/>Topic: The Enemies of The End-Times Church <br/>Subtitles: <br/> -How the antichrist raises an army by social behavior engineering. <br/>-How the architects of modern social constructs escaped the church's radar. <br/>-The Holy Spirit's end-times agenda:<br/> The Knock-Out Punch!<br/>Speaker: Prophet Marcus Toliver <br/>Dates/time: December 27, 28 & 29 at 6pm<br/>Location: Halvorn Community Center <br/> 241 Pellham Street <br/> Portland, ME 04102<br/>Contact info: phone: 207-555-0148 <br/>email: contact@brookmeadow.example <br/> www.vutel.example<br/>*The flyer must also include a picture of the speaker and our Vutel logo <br/>Thanks, we look forward to seeing what you come up with!

Colors

Designer to choose colors to be used in the design.

Requirements
Must have
• The flyer must include all of the following:
• Title: Kestrel Summit 2019
• Topic: The Enemies of The End-Times Church
• Subtitles:
• -How the antichrist raises an army by social behavior engineering.
• -How the architects of modern social constructs escaped the church's radar.
• -The Holy Spirit's end-times agenda:
• The Knock-Out Punch!
• Speaker: Prophet Marcus Toliver
• Dates/time: December 27, 28 & 29 at 6pm
• Location: Halvorn Community Center
• 241 Pellham Street
• Portland, ME 04102
• Contact info: phone: 207-555-0148
• email: contact@brookmeadow.example
• www.vutel.example
• *The flyer must also include a picture of the speaker and our Vutel logo
Should not have
• Pictures of crosses or church buildings

```html
<!DOCTYPE html>
<html lang="en">
<head>
<meta charset="utf-8">
<title>Kestrel Summit 2019 Flyer</title>
<link href="https://fonts.googleapis.com/css2?family=Great+Vibes&family=Poppins:wght@400;500;600;700;800&family=Cinzel:wght@500&display=swap" rel="stylesheet">
<style>
  :root{
    --bg:#c9bb9e;
    --red:#b30d12;
    --red-deep:#8a070b;
    --red-dark:#6a0508;
    --gold:#e7b93a;
    --gold-light:#f6d36a;
    --gold-text:#e9bd45;
    --ink-red:#a0080d;
    --white:#ffffff;
  }
  *{margin:0;padding:0;box-sizing:border-box}
  html,body{width:1200px;height:960px;overflow:hidden;background:var(--bg)}
  .flyer{
    position:absolute;left:282px;top:30px;width:636px;height:900px;
    background:linear-gradient(180deg,var(--red) 0%,var(--red-deep) 100%);
    overflow:hidden;font-family:"Poppins",sans-serif;color:var(--white);
    box-shadow:0 10px 30px rgba(80,60,30,.25);
  }
  .photo-wash{position:absolute}
  .photo-wash--top{right:0;top:0;width:340px;height:300px;
    background:radial-gradient(ellipse at 60% 45%,rgba(220,40,40,.55),rgba(179,13,18,0) 70%)}
  .photo-wash--bottom{left:0;top:600px;width:280px;height:220px;
    background:radial-gradient(ellipse at 40% 50%,rgba(200,30,30,.45),rgba(138,7,11,0) 70%)}
  .site-top{position:absolute;top:22px;width:100%;text-align:center;font-size:13px}
  .brand{position:absolute;top:52px;width:100%;display:flex;justify-content:center;align-items:center;gap:10px}
  .brand-dot{width:14px;height:14px;border-radius:50%;background:var(--white)}
  .brand-name{font-family:"Cinzel",serif;font-weight:500;font-size:52px;letter-spacing:1px;line-height:1}
  .title{position:absolute;top:150px;width:100%;text-align:center;font-family:"Great Vibes",cursive;
    font-size:66px;color:var(--gold-text);line-height:1}
  .band{position:absolute;left:0;top:0}
  .topic{position:absolute;top:292px;left:40px;right:40px;text-align:center;color:var(--ink-red)}
  .topic-head{font-weight:800;font-size:22px;letter-spacing:-.2px;line-height:1.2}
  .topic-line{font-weight:500;font-size:18px;line-height:1.3}
  .speaker-photo{position:absolute;left:258px;top:482px;width:120px;height:120px;border-radius:50%;
    border:5px solid var(--gold);background:radial-gradient(circle at 50% 40%,#6d6560,#3c3735 60%,#8e8b88);}
  .ribbon{position:absolute;left:0;top:0}
  .speaker-label{position:absolute;top:607px;width:100%;text-align:center;font-size:13px;letter-spacing:5px}
  .speaker-name{position:absolute;top:624px;width:100%;text-align:center;font-size:22px;font-weight:500;color:var(--gold-text)}
  .dates{position:absolute;top:680px;width:100%;text-align:center;font-weight:800;font-size:44px;color:var(--gold-text);
    text-shadow:0 3px 4px rgba(60,0,0,.45);line-height:1}
  .time{position:absolute;top:734px;width:100%;text-align:center;font-weight:700;font-size:22px;color:var(--gold-text);
    text-shadow:0 2px 3px rgba(60,0,0,.45)}
  .location{position:absolute;top:780px;width:100%;text-align:center;font-size:13px;letter-spacing:2px;line-height:1.35}
  .location-label{font-weight:700}
  .location-street{font-weight:700}
  .contact{position:absolute;bottom:18px;left:20px;right:20px;display:flex;justify-content:space-around;align-items:center;font-size:13px}
  .contact-sep{width:1px;height:28px;background:var(--white)}
</style>
</head>
<body>
  <main class="flyer">
    <div class="photo-wash photo-wash--top" role="img" aria-label="Faint red-toned portrait of the speaker"></div>
    <div class="photo-wash photo-wash--bottom" role="img" aria-label="Faint red-toned portrait of the speaker"></div>

    <p class="site-top">www.vutel.example</p>
    <div class="brand"><span class="brand-dot"></span><span class="brand-name">VUTEL</span></div>
    <h1 class="title">Kestrel Summit 2019</h1>

    <svg class="band" width="636" height="900" viewBox="0 0 636 900" aria-hidden="true">
      <defs>
        <linearGradient id="goldBand" x1="0" y1="0" x2="1" y2="0">
          <stop offset="0" stop-color="#dcaa28"/>
          <stop offset=".55" stop-color="#f2c95a"/>
          <stop offset="1" stop-color="#f8d978"/>
        </linearGradient>
      </defs>
      <path d="M0 272 Q300 300 636 212 L636 530 Q330 520 0 590 Z" fill="url(#goldBand)"/>
    </svg>

    <section class="topic">
      <h2 class="topic-head">THE ENEMIES OF THE END-TIMES CHURCH</h2>
      <p class="topic-line">How the antichrist raises an army by social behavior engineering.</p>
      <p class="topic-line">How the architects of modern social constructs escaped the church's radar.</p>
      <p class="topic-line">The Holy Spirit's end-times agenda.<br>The Knock-Out Punch!</p>
    </section>

    <div class="speaker-photo" role="img" aria-label="Portrait photo of the speaker, Prophet Marcus Toliver"></div>

    <svg class="ribbon" width="636" height="900" viewBox="0 0 636 900" aria-hidden="true">
      <path d="M150 612 L486 612 L506 634 L486 656 L150 656 L130 634 Z" fill="var(--red-dark)"/>
      <path d="M170 604 L466 604 L466 660 L170 660 Z" fill="#7a060a"/>
    </svg>
    <p class="speaker-label">SPEAKER</p>
    <p class="speaker-name">Prophet Marcus Toliver</p>

    <p class="dates">DECEMBER 27, 28 &amp; 29</p>
    <p class="time">STARTING AT 18:00h</p>

    <address class="location" style="font-style:normal">
      <span class="location-label">LOCATION</span><br>
      Halvorn Community Center<br>
      <span class="location-street">241 Pellham Street</span><br>
      Portland, ME 04102
    </address>

    <footer class="contact">
      <span>contact@brookmeadow.example</span>
      <span class="contact-sep"></span>
      <span>www.vutel.example</span>
      <span class="contact-sep"></span>
      <span>207-555-0148</span>
    </footer>
  </main>
</body>
</html>
```